Curantel System Web Page Design

This project is to design 6 pages of a web based medical system for clinics, hospitals, drugs suppliers, general items suppliers, insurance company, laboratories and patients (basically all parties which could be involved in).We want the designs of the browser, button, icon and layout are based on Oru, which is user friendly, looks professional, simple and neat but with powerful functions. We have uploaded few pictures of another system, please do not copy its design because this is not what we are looking for, the pictures are for you to know the elements should be included in our pages. Curantel web-base system, design 6 pages1. Login PageShould include the following elements-company id with input field-login id with input field-password with input field2. Main Page (Navigation page)Should include the following elements-Appointment-Consultation-Patient-Drugs inventory -General supplies inventory -Laboratory-Suppliers-Insurance-Reports 3. Appointment PageShould include all the the elements in the respective pictures plus the followings-Daily View, Weekly View, Monthly View buttons4. Consultation PageShould include all the the elements in the respective picture5. Patient Page5.1 General information Should include all the the elements in the respective picture5.2 medical history/lab reportsShould include all the the elements in the respective picture plus the followings-Notify patient button-Share report button.
Please stop using Ward Harbor in your designs which is not the name of our system. We have just rename our system to Curantel, please take note.
We need the system to look professional not playful, do not use too many colors and playful icons.
professional users
5+ page

```html
<!DOCTYPE html>
<html lang="en">
<head>
<meta charset="utf-8">
<title>Curantel – Main Navigation</title>
<link href="https://fonts.googleapis.com/css2?family=Open+Sans:wght@400;500;600;700&display=swap" rel="stylesheet">
<style>
  :root {
    --page-bg: #ffffff;
    --side-top: #15305a;
    --side-bottom: #17485f;
    --side-band: #0c1a2c;
    --side-links: #0a1522;
    --side-line: #1b2a3c;
    --accent: #f0941f;
    --info: #3cc3e6;
    --main-top: #1c55c6;
    --main-mid: #2a83c9;
    --main-bottom: #27b6c9;
    --tile-fill: rgba(255,255,255,0.07);
    --tile-line: rgba(255,255,255,0.16);
    --tile-active: #d98a2f;
    --text: #ffffff;
    --muted: #8ea4bc;
  }
  * { box-sizing: border-box; margin: 0; padding: 0; }
  html, body { width: 1200px; height: 1200px; overflow: hidden; background: var(--page-bg); }
  body { font-family: "Open Sans", Arial, sans-serif; color: var(--text); }

  .app {
    position: absolute; top: 226px; left: 0;
    width: 1200px; height: 750px; display: flex;
  }

  .sidebar {
    width: 201px; height: 100%; position: relative;
    background: linear-gradient(180deg, var(--side-top) 0%, var(--side-top) 45%, var(--side-bottom) 100%);
  }
  .brand {
    position: absolute; top: 36px; width: 100%; text-align: center;
    font-size: 24px; font-weight: 700; letter-spacing: 0.3px;
  }
  .languages {
    position: absolute; top: 81px; width: 100%;
    display: flex; justify-content: center; gap: 6px;
  }
  .languages span { width: 14px; height: 10px; display: block; }
  .lang-en { background: #3a4f8f; border: 1px solid #d9dde8; }
  .lang-zh { background: #d8261c; }
  .avatar {
    position: absolute; top: 143px; left: 78px; width: 46px; height: 46px;
    border-radius: 50%; border: 3px solid #243f66;
    background: radial-gradient(circle at 50% 40%, #e8e2dc 0%, #9d958f 60%, #2c2c2c 100%);
  }
  .user-name {
    position: absolute; top: 196px; width: 100%; text-align: center;
    font-size: 13px; font-weight: 600; letter-spacing: 0.5px; color: #e6ecf3;
  }
  .user-date {
    position: absolute; top: 216px; width: 100%; text-align: center;
    font-size: 9px; color: var(--muted);
  }
  .user-date sup { font-size: 6px; }
  .context {
    position: absolute; top: 276px; width: 100%; height: 70px;
    background: var(--side-band); padding: 17px 0 0 22px;
    font-size: 10.5px; color: var(--info); line-height: 21px; text-transform: uppercase;
  }
  .nav { position: absolute; top: 346px; width: 100%; list-style: none; }
  .nav li {
    height: 33px; line-height: 33px; padding-left: 22px;
    font-size: 10px; background: var(--side-links);
    border-bottom: 1px solid var(--side-line);
  }
  .nav li.is-active { color: var(--accent); border-right: 2px solid var(--accent); background: #070f19; }
  .logout {
    position: absolute; top: 671px; left: 22px;
    display: flex; align-items: center; gap: 9px; font-size: 11.5px;
  }

  .main {
    flex: 1; height: 100%; position: relative; overflow: hidden;
    background: linear-gradient(205deg, var(--main-top) 0%, var(--main-mid) 45%, var(--main-bottom) 100%);
  }
  .main::before {
    content: ""; position: absolute; inset: 0;
    background: linear-gradient(135deg, rgba(255,255,255,0.08) 0%, rgba(255,255,255,0.08) 45%, rgba(255,255,255,0) 45.1%);
  }
  .hotline {
    position: absolute; top: 36px; right: 66px;
    display: flex; align-items: baseline; gap: 14px;
  }
  .hotline-label { font-size: 16px; color: #dce8f7; }
  .hotline-number { font-size: 26px; font-weight: 700; }

  .modules {
    position: absolute; top: 106px; left: 88px;
    display: grid; grid-template-columns: repeat(3, 244px);
    grid-template-rows: repeat(3, 184px); column-gap: 16px; row-gap: 14px;
  }
  .module {
    position: relative; background: var(--tile-fill); border: 1px solid var(--tile-line);
    text-align: center;
  }
  .module.is-active { background: var(--tile-active); border-color: var(--tile-active); }
  .module-icon {
    position: absolute; top: 46px; left: 92px; width: 60px; height: 60px;
    border-radius: 4px;
    background: linear-gradient(160deg, rgba(255,255,255,0.30), rgba(240,148,31,0.22));
  }
  .module.is-active .module-icon {
    background: linear-gradient(160deg, rgba(20,25,35,0.45), rgba(20,25,35,0.25));
  }
  .module-label {
    position: absolute; top: 128px; width: 100%;
    font-size: 17.5px; font-weight: 500; line-height: 19px; letter-spacing: 0.3px;
  }
</style>
</head>
<body>
<div class="app">
  <aside class="sidebar">
    <div class="brand">Curantel</div>
    <div class="languages"><span class="lang-en"></span><span class="lang-zh"></span></div>
    <div class="avatar" role="img" aria-label="User profile photo"></div>
    <div class="user-name">Daniel Hartley</div>
    <div class="user-date">Date: 27<sup>th</sup> Nov. 2018</div>
    <div class="context">
      Clinic : Medvale<br>
      Doctor : Helen Morrow
    </div>
    <ul class="nav">
      <li class="is-active">Link 1</li>
      <li>Link 2</li>
      <li>Link 3</li>
      <li>Link 3</li>
    </ul>
    <div class="logout">
      <svg width="22" height="22" viewBox="0 0 22 22" fill="none" stroke="#ffffff" stroke-width="1.4">
        <path d="M15 5.5A8 8 0 1 0 15 16.5"/>
        <path d="M8 11h12M16.5 7.5 20 11l-3.5 3.5"/>
      </svg>
      Logout
    </div>
  </aside>

  <main class="main">
    <div class="hotline">
      <span class="hotline-label">Support hotline</span>
      <span class="hotline-number">(852) 2460 5198</span>
    </div>

    <section class="modules">
      <div class="module">
        <div class="module-icon" role="img" aria-label="Appointment calendar icon"></div>
        <div class="module-label">Appointment</div>
      </div>
      <div class="module is-active">
        <div class="module-icon" role="img" aria-label="Consultation icon"></div>
        <div class="module-label">Consultation</div>
      </div>
      <div class="module">
        <div class="module-icon" role="img" aria-label="Patient icon"></div>
        <div class="module-label">Patient</div>
      </div>
      <div class="module">
        <div class="module-icon" role="img" aria-label="Drugs inventory icon"></div>
        <div class="module-label">Drugs Inventory</div>
      </div>
      <div class="module">
        <div class="module-icon" role="img" aria-label="General supplies shelf icon"></div>
        <div class="module-label">General Supplies<br>Inventory</div>
      </div>
      <div class="module">
        <div class="module-icon" role="img" aria-label="Laboratory flask icon"></div>
        <div class="module-label">Laboratory</div>
      </div>
      <div class="module">
        <div class="module-icon" role="img" aria-label="Suppliers medicine bottle icon"></div>
        <div class="module-label">Suppliers</div>
      </div>
      <div class="module">
        <div class="module-icon" role="img" aria-label="Insurance umbrella icon"></div>
        <div class="module-label">Insurance</div>
      </div>
      <div class="module">
        <div class="module-icon" role="img" aria-label="Reports folder icon"></div>
        <div class="module-label">Reports</div>
      </div>
    </section>
  </main>
</div>
</body>
</html>
```